Powerpoint to present for client our social media services along with a test case

we need a powerpoint template design that is modern looking and eye catching and keeps the client engaged. we are a social media agency based in Kuwait so the content will be bilingual in english and in Arabic. i will be providing the logo and you can design based upon the logo provided. the main tasks for this PPT is to show case our case studies and for sales presentation. the presentations will be a mix of visuals, texts, graphs and charts.
the ppt design has to reflect the company colors in the logo with the logo scattered to show it is done by the company.

It Company

```html
<!DOCTYPE html>
<html lang="en">
<head>
<meta charset="utf-8">
<title>Lumora Media – Informations</title>
<link rel="stylesheet" href="https://fonts.googleapis.com/css2?family=Questrial&family=Arimo:wght@400&display=swap">
<style>
  :root {
    --bg-top: #ffffff;
    --bg-bottom: #e6e6e6;
    --ink: #2b2b2b;
    --ink-soft: #555555;
    --rule: #a8a8a8;
    --brand-red: #e01b24;
    --head-red: #c4161c;
    --brand-green: #7aa62a;
    --brand-blue: #2a7fc1;
    --brand-orange: #f0960e;
    --brand-purple: #8a4fa3;
  }
  * { margin: 0; padding: 0; box-sizing: border-box; }
  html, body { width: 1200px; height: 833px; overflow: hidden; }
  body {
    font-family: "Arimo", Arial, sans-serif;
    color: var(--ink);
    background: var(--bg-bottom);
  }
  .slide {
    position: relative;
    width: 1200px;
    height: 833px;
    overflow: hidden;
    background: linear-gradient(to bottom, var(--bg-top) 0%, #f3f3f3 40%, var(--bg-bottom) 100%);
  }
  .rule {
    position: absolute;
    top: 89px;
    height: 1px;
    background: var(--rule);
  }
  .rule--left { left: 0; width: 36px; }
  .rule--mid { left: 268px; width: 514px; }

  .brand {
    position: absolute;
    left: 44px;
    top: 50px;
    height: 44px;
    display: flex;
    align-items: center;
    gap: 10px;
  }
  .brand__dot {
    width: 44px;
    height: 44px;
    border-radius: 50%;
    background: var(--brand-red);
  }
  .brand__name {
    font-family: "Questrial", "Century Gothic", sans-serif;
    font-size: 26px;
    color: var(--ink);
    white-space: nowrap;
  }

  .tagline {
    position: absolute;
    right: 42px;
    top: 76px;
    font-family: "Questrial", "Century Gothic", sans-serif;
    font-size: 22px;
    line-height: 24px;
    color: var(--ink);
    white-space: nowrap;
  }
  .tagline__mark {
    position: absolute;
    right: 0;
    top: 80px;
    width: 30px;
    height: 16px;
    background: var(--brand-red);
  }

  .content {
    position: absolute;
    left: 69px;
    top: 178px;
    width: 617px;
  }
  .content__title {
    font-family: "Questrial", "Century Gothic", sans-serif;
    font-weight: 400;
    font-size: 33px;
    line-height: 40px;
    color: var(--head-red);
    margin-bottom: 14px;
  }
  .content__title small { font-size: 20px; }
  .content p {
    font-size: 15.4px;
    line-height: 19.3px;
    text-align: justify;
    color: var(--ink);
    margin-bottom: 17px;
  }

  .feature-photo {
    position: absolute;
    left: 745px;
    top: 262px;
    width: 300px;
    height: 300px;
    border-radius: 50%;
    background: radial-gradient(circle at 50% 40%, #f4f1ec 0%, #d9d4cc 60%, #b9b4ad 100%);
  }

  .footer__copy,
  .footer__url {
    position: absolute;
    top: 793px;
    font-size: 16px;
    color: var(--ink-soft);
  }
  .footer__copy { left: 16px; }
  .footer__url { right: 17px; }

  .colour-bar {
    position: absolute;
    left: 0;
    bottom: 0;
    width: 1200px;
    height: 9px;
    display: flex;
  }
  .colour-bar span { flex: 1; }
  .colour-bar .red { background: var(--brand-red); }
  .colour-bar .green { background: var(--brand-green); }
  .colour-bar .blue { background: var(--brand-blue); }
  .colour-bar .orange { background: var(--brand-orange); }
  .colour-bar .purple { background: var(--brand-purple); }
</style>
</head>
<body>
<main class="slide">
  <div class="rule rule--left"></div>
  <div class="rule rule--mid"></div>

  <div class="brand">
    <span class="brand__dot"></span>
    <span class="brand__name">Lumora Media</span>
  </div>

  <div class="tagline">TAGLINE WILL BE REPLACED HERE</div>
  <div class="tagline__mark"></div>

  <section class="content">
    <h1 class="content__title">INFORMATIONS <small>(HEADER)</small></h1>
    <p>Lorem ipsum dolor sit amet, consectetur adipiscing elit. Ut vulputate leo sit amet lacus volutpat, vel rutrum nisl adipiscing. Morbi at imperdiet magna. Interdum et malesuada fames ac ante ipsum primis in faucibus. Vestibulum feugiat ullamcorper tincidunt. Morbi enim lorem, hendrerit quis convallis eget, dapibus a ante. Integer porta leo consequat</p>
    <p>metus sagittis, aliquet aliquam nulla interdum. Vestibulum eu bibendum nulla. orem</p>
    <p>ipsum dolor sit amet, consectetur adipiscing elit. Ut vulputate leo sit amet lacus volutpat, vel rutrum nisl adipiscing. Morbi at imperdiet magna. Interdum et malesuada fames ac ante ipsum primis in faucibus. Vestibulum feugiat ullamcorper tincidunt. Morbi enim lorem, hendrerit quis convallis eget, dapibus a ante. Integer porta leo consequat metus sagittis, aliquet aliquam nulla interdum. Vestibulum eu bibendum nulla.</p>
    <p>Lorem ipsum dolor sit amet, consectetur adipiscing elit. Ut vulputate leo sit amet lacus volutpat, vel rutrum nisl adipiscing. Morbi at imperdiet magna. Interdum et malesuada fames ac ante ipsum primis in faucibus. Vestibulum feugiat ullamcorper tincidunt. Morbi enim lorem, hendrerit quis convallis eget, dapibus a ante. Integer porta leo consequat metus sagittis, aliquet aliquam null</p>
    <p>Lorem ipsum dolor sit amet, consectetur adipiscing elit. Ut vulputate leo sit amet lacus volutpat, vel rutrum nisl adipiscing. Morbi at imperdiet magna. Interdum et malesuada fames ac ante ipsum primis in faucibus.</p>
    <p>Vestibulum feugiat ullamcorper tincidunt. Morbi enim lorem, hendrerit quis convallis eget, dapibus a ante. Integer porta leo consequat metus sagittis, aliquet aliquam null</p>
  </section>

  <div class="feature-photo" role="img" aria-label="Photo of a smiling team of young professionals standing together under social network speech bubbles"></div>

  <div class="footer__copy">© 2014 Lumora Media</div>
  <div class="footer__url">http://www.lumoramedia.com</div>

  <div class="colour-bar">
    <span class="red"></span>
    <span class="green"></span>
    <span class="blue"></span>
    <span class="orange"></span>
    <span class="purple"></span>
  </div>
</main>
</body>
</html>
```